Lantern over the Harbor ~ A Widening Passage for Writers

My book is called “Lantern over the Harbor.” Its subtitle is “A Widening Passage for Writers.” It is a book about being a poet, writing poetry, and the ways in which poets are connected to both society and the central energy of the Universe. I want the cover design to be abstract and impressionistic. A suggestion of fireworks or a starburst would be a plus. To be consistent with the 3 other books I have published, I want the font for the title, as well as my name (Dorothea Quillbrake) to be Papyrus. The subtitle font can be something more plain and sans serif, like Arial or Franklin Gothic Book, probably in italics. As for color, I definitely want pale gold (angelic). Possible other complimentary colors could be either light or dark shades of gray, turquoise, rose, rust or red. I'm attaching the back cover text and also three pages from inside the book that have line drawings, to give an example of the interior artwork.
Updates

Forgot to mention: My book is a paperback. Its size will be 8.5" high and 5.5" wide. I'm self-publishing it, and it will be printed by Halvern Printworks in Nebraska, USA. It has 104 pages. I think you need the number of pages, in order to make the spine of the book the correct width.

Target Market(s)

My target market is people who write poetry or are interested in how poetry is written.

Industry/Entity Type

Poetry

Font styles to use
Sans Serif
Other font styles liked:
• Papyrus for the front cover. Arial or another sans serif font on the back cover.

Colors

Designer to choose colors to be used in the design.

Requirements
Must have
• My book cover needs to be inspiring and uplifting, as well as abstract and impressionistic, with kind of a "New Age" feel. I don't want anything that looks rigid and scholarly.
Nice to have
• The book talks about the connection poets have to the Universe and the Creative Energy at the center of everything. The cover should convey that Energy.
Should not have
• My cover should not be realistic, logical or straight-laced. I want something that feels free, imaginative and unfettered.

```html
<!DOCTYPE html>
<html lang="en">
<head>
<meta charset="utf-8">
<title>Lantern over the Harbor — Dorothea Quillbrake</title>
<link rel="stylesheet" href="https://fonts.googleapis.com/css2?family=Josefin+Sans:wght@400;600;700&display=swap">
<style>
  :root {
    --paper: #ebe4d8;
    --gold: #d9bd7c;
    --gold-deep: #c9a65e;
    --rust: #c9674a;
    --turquoise: #6fb3ad;
    --ink: #1c1a17;
    --wine: #7a1f1c;
    --rule: #4a4540;
  }
  * { margin: 0; padding: 0; box-sizing: border-box; }
  html, body {
    width: 678px;
    height: 1200px;
    overflow: hidden;
    background: var(--paper);
  }
  .cover {
    position: relative;
    width: 678px;
    height: 1200px;
    background: var(--paper);
    font-family: "Josefin Sans", sans-serif;
    color: var(--ink);
  }
  .cover__burst {
    position: absolute;
    left: 0;
    top: 0;
    width: 678px;
    height: 1030px;
    background: radial-gradient(ellipse 330px 440px at 320px 470px,
      var(--gold) 0%,
      var(--gold-deep) 30%,
      rgba(201,166,94,0.55) 52%,
      rgba(201,103,74,0.25) 72%,
      rgba(111,179,173,0.12) 85%,
      rgba(235,228,216,0) 100%);
  }
  .cover__title {
    position: absolute;
    left: 0;
    width: 678px;
    top: 410px;
    text-align: center;
    font-weight: 700;
    font-size: 46px;
    line-height: 82px;
    letter-spacing: 1px;
    text-transform: uppercase;
  }
  .cover__title .light { font-weight: 400; }
  .cover__title-line { display: block; }
  .cover__title-line--first { padding-right: 40px; }
  .cover__subtitle {
    position: absolute;
    left: 0;
    width: 678px;
    top: 1038px;
    text-align: center;
    font-weight: 600;
    font-size: 22px;
    text-transform: uppercase;
    letter-spacing: 0.3px;
  }
  .cover__subtitle-echo {
    position: absolute;
    left: 0;
    width: 678px;
    top: 1068px;
    text-align: center;
    font-weight: 400;
    font-size: 17px;
    color: var(--wine);
  }
  .cover__rule {
    position: absolute;
    left: 114px;
    top: 1100px;
    width: 402px;
    height: 1px;
    background: var(--rule);
  }
  .cover__author {
    position: absolute;
    left: 0;
    width: 678px;
    top: 1124px;
    text-align: center;
    font-weight: 700;
    font-size: 21px;
    letter-spacing: 0.5px;
    text-transform: uppercase;
  }
</style>
</head>
<body>
  <main class="cover">
    <div class="cover__burst" role="img" aria-label="Abstract watercolour starburst in pale gold with rust and turquoise strokes and fine radiating ink lines"></div>
    <h1 class="cover__title">
      <span class="cover__title-line cover__title-line--first">Lantern <span class="light">over</span></span>
      <span class="cover__title-line">the Harbor</span>
    </h1>
    <p class="cover__subtitle">A Widening Passage for Writers</p>
    <p class="cover__subtitle-echo">A Widening Passage For Writers</p>
    <div class="cover__rule"></div>
    <p class="cover__author">Dorothea Quillbrake</p>
  </main>
</body>
</html>
```